Web Design job - NetQuarry Company including Desktop & Mobile version

Create a Web Design (Uncoded - PSD layout only)

1. About our company

NetQuarry is an Australian-based company which sells used networking devices to coporates and other brokers in USA, Europe and other countries. We are the market leader in this space and currently have warehouses in Sydney and California. Most of our products are from VORNEX.

Our competitive advantages come from lowest price in the market, flexible product configuration for different demands of customers, long time experience in the business and huge stock of inventory.

We are in need of a new website to enhance customer and partner engagement which are measured by sales metrics and website performance metrics such as number of request for a quote, number of new orders, return visits, views, conversion rate, etc.

2. Website structure:

We need different looks for different devices: Desktop, iPad and Mobile with popular screen resolutions for each of following page.

Try to make one as good as possible, then we can move further. Below are the main pages of the web:

+ Home Page: Where customers learn about the company and its business. Should have: Beautiful company profile, highlighted company contact and strengths; A comprehensive overview about selling products.

+ Category Page: Where customers learn about products in a category and do the search action. Should focus on filter and sort functions for easily finding a product.

+ Product Page: Where customers learn about the details of a specific products such as price, image, description, related products.
- Also need features for cross-sell or up-sell.
- An item may have both new and refurbished prices, or either or none of them. Should have options to choose between new or refurbished price to add to cart.

+ Information Page: About the company, Company Announcement.

+ Cart management and Check-out

+ Search results

REFERENCES
Current website: http://netquarry-example.com.au/

Prefered Layout:
- https://www.gearplaza-example.com/en/vornex-gear/vornex-router-series/vornex-series-4700/vornex-gear-vornex4783-m2
- https://www.wiresandbins-example.com/vornex-2port-rj48-duolink-t1-trunk-card-qzlt2dhhq2-p-5826.html
- The attached files play as wireframes, only for the purpose of guiding. You are free to make your choices of colors and layouts.

Target Market(s)

- Corporate clients
- Main market: Australia

Industry/Entity Type

It Company

Number of Pages Required

3 page

Font styles to use
Sans Serif

Requirements
Must have
• - The new design should have a clear look to easily find information while should look professional to aim at corporate clients.
• - Require least time or effort to finish a task
• - Optimize for SEO and loading time
• - Mobile version is optimized for touching, swiping and loading time.
• - Bear in mind that the new website need minimum effort of manual tasks such as updating content. We don’t have human resources for these yet.
Nice to have
• - Should have design for each scenario such as click, popup, dropdown, deactive, have/not have an object

```html
<!DOCTYPE html>
<html lang="en">
<head>
<meta charset="utf-8">
<title>NetQuarry – Networking Equipment</title>
<link href="https://fonts.googleapis.com/css2?family=Roboto:wght@300;400;500;700&display=swap" rel="stylesheet">
<style>
:root{
  --blue:#1b9be0;
  --navy:#0d3f94;
  --orange:#f7892b;
  --yellow:#f8c21a;
  --red:#e8322c;
  --ink:#2a2a2a;
  --muted:#7a7a7a;
  --grey-bg:#efefef;
  --line:#dedede;
}
*{margin:0;padding:0;box-sizing:border-box}
html,body{width:754px;height:1200px;overflow:hidden}
body{font-family:'Roboto',sans-serif;color:var(--ink);background:#fff;position:relative}

/* header */
.site-header{position:absolute;left:0;top:0;width:754px;height:56px;background:#fff}
.brand{position:absolute;left:70px;top:12px;display:flex;align-items:center;gap:7px}
.brand-dot{width:26px;height:26px;border-radius:50%;background:var(--orange)}
.brand-name{font-size:20px;font-weight:700;color:var(--navy)}
.header-item{position:absolute;top:16px;display:flex;gap:6px;font-size:9px;line-height:11px;white-space:nowrap}
.header-item strong{font-weight:500;display:block}
.header-item span{color:#666;font-size:8.5px}
.header-item svg{flex:none;margin-top:1px}
.quote-btn{position:absolute;left:596px;top:16px;width:88px;height:23px;background:var(--orange);color:#fff;font-size:10px;font-weight:500;display:flex;align-items:center;justify-content:center}

/* nav */
.main-nav{position:absolute;left:0;top:56px;width:754px;height:26px;background:var(--blue)}
.main-nav ul{list-style:none;position:absolute;left:70px;top:0;display:flex;height:26px}
.main-nav li{color:#fff;font-size:10px;font-weight:500;padding:0 9.5px;line-height:26px}
.main-nav li.active{background:var(--orange)}
.search{position:absolute;left:457px;top:3px;width:227px;height:20px;background:#fff;border-radius:10px;font-size:7.5px;color:#999;padding:0 11px;line-height:20px}
.search svg{position:absolute;right:7px;top:5px}

/* hero */
.hero{position:absolute;left:0;top:82px;width:754px;height:296px;background:linear-gradient(160deg,#f7fafc 0%,#e8eff5 55%,#f3f6f9 100%);overflow:hidden}
.hero-swoosh{position:absolute;left:0;top:0}
.hero-art{position:absolute;left:92px;top:54px;width:316px;height:196px;background:linear-gradient(180deg,#5f6b78,#2d3540);border-radius:3px}
.hero-title{position:absolute;left:400px;top:86px;width:268px;text-align:center;font-size:27px;font-weight:300;color:var(--blue)}
.hero-title b{font-weight:400;color:var(--orange)}
.hero-sub{position:absolute;left:400px;top:122px;width:268px;text-align:center;font-size:10px;font-weight:500;color:#333}
.hero-sub em{font-style:normal;color:var(--blue)}
.stock-btn{position:absolute;left:494px;top:156px;width:82px;height:23px;background:var(--orange);border-radius:12px;color:#fff;font-size:9.5px;font-weight:500;line-height:23px;padding-left:14px}
.stock-btn i{position:absolute;right:5px;top:5px;width:13px;height:13px;border-radius:50%;background:#fff}
.stock-btn i:after{content:"";position:absolute;left:4px;top:3.5px;border-left:5px solid var(--orange);border-top:3px solid transparent;border-bottom:3px solid transparent}
.dots{position:absolute;left:637px;top:272px;display:flex;gap:3px}
.dots span{width:7px;height:7px;border-radius:50%;border:1px solid #aaa}
.dots span.on{background:var(--orange);border-color:var(--orange)}

/* categories */
.categories{position:absolute;left:0;top:378px;width:754px;height:112px;background:var(--orange)}
.section-title-light{position:absolute;top:10px;width:754px;text-align:center;color:#fff;font-size:12px;font-weight:500}
.cat-card{position:absolute;top:32px;width:150px;height:76px;background:#fff;display:flex;align-items:center}
.cat-thumb{width:67px;height:60px;margin-left:6px;background:linear-gradient(180deg,#d7dbe0,#9aa2ab);border-radius:2px;flex:none}
.cat-name{font-size:9px;font-weight:500;margin-left:8px;line-height:10px}
.cat-card.active .cat-name{color:var(--orange)}
.pointer{position:absolute;left:139px;top:112px;border-top:6px solid var(--orange);border-left:6px solid transparent;border-right:6px solid transparent}

/* products */
.products{position:absolute;left:0;top:490px;width:754px;height:206px;background:var(--grey-bg)}
.product-card{position:absolute;top:14px;width:142px;height:160px;background:#fff;text-align:center}
.product-img{width:84px;height:62px;margin:11px auto 0;background:linear-gradient(180deg,#cfd4da,#6f7985);border-radius:4px}
.product-name{margin-top:19px;font-size:9px;font-weight:500}
.price{font-size:7.5px;color:#444;margin-top:5px;line-height:13px}
.price b{font-weight:400;color:var(--red)}
.save{font-size:7.5px;color:#999}
.view-more{position:absolute;left:601px;top:185px;font-size:7.5px;color:var(--blue);text-decoration:underline}
.view-more:after{content:"";display:inline-block;margin-left:3px;border-left:4px solid var(--blue);border-top:3px solid transparent;border-bottom:3px solid transparent}

/* welcome */
.welcome-title{position:absolute;left:70px;top:726px;font-size:12px;font-weight:500}
.stat{position:absolute;left:70px;width:158px;display:flex;align-items:center;gap:5px;border-bottom:1px solid var(--line);padding-bottom:7px}
.stat .num{font-size:25px;color:var(--orange);font-weight:400}
.stat .num small{font-size:12px}
.stat .lbl{font-size:9px;line-height:11px;color:#333}
.stat.last{border:0}
.about-text{position:absolute;left:244px;top:756px;width:124px;font-size:7.5px;line-height:13px;color:#555}
.about-text strong{font-weight:500;color:#333}
.read-more{position:absolute;left:244px;top:922px;font-size:7.5px;color:#333;text-decoration:underline}
.read-more:after{content:"";display:inline-block;margin-left:4px;border-left:4px solid var(--blue);border-top:3px solid transparent;border-bottom:3px solid transparent}
.quote-box{position:absolute;left:385px;top:728px;width:299px;height:204px;background:#ececec;overflow:hidden}
.quote-corner{position:absolute;right:0;top:0;border-top:30px solid var(--blue);border-left:30px solid transparent}
.agent{position:absolute;left:8px;top:24px;width:112px;height:180px;background:linear-gradient(180deg,#d9c3b4 0%,#2a9aa8 55%,#1c8997 100%);border-radius:50px 50px 0 0}
.quote-body{position:absolute;left:118px;top:36px;width:176px;text-align:center}
.quote-body h3{font-size:12px;font-weight:500}
.quote-phone{font-size:15px;color:var(--orange);margin-top:14px}
.quote-note{font-size:8.5px;line-height:10px;margin-top:4px;color:#333}
.quote-or{font-size:7px;color:#555;margin-top:9px}
.quote-mail{font-size:10px;color:var(--blue);margin-top:4px;font-weight:500}

/* policy buttons */
.policy{position:absolute;top:973px;width:200px;height:43px;color:#fff;font-size:12.5px;font-weight:700;display:flex;align-items:center;justify-content:center;gap:6px}
.policy i{width:11px;height:11px;border:1.3px solid #fff;border-radius:50%;position:relative}
.policy i:after{content:"";position:absolute;left:3.2px;top:2px;border-left:3.5px solid #fff;border-top:2.5px solid transparent;border-bottom:2.5px solid transparent}

/* footer */
.site-footer{position:absolute;left:0;top:1024px;width:754px;height:176px;background:var(--navy);color:#fff}
.footer-title{position:absolute;font-size:9px;font-weight:500}
.footer-about{position:absolute;left:70px;top:38px;width:160px;font-size:7.5px;line-height:10.8px;color:#a9bbd9}
.contact-list{position:absolute;left:280px;top:38px;list-style:none;font-size:7.5px;color:#b9c8e2}
.contact-list li{display:flex;gap:8px;align-items:center;height:19.3px;white-space:nowrap}
.contact-list svg{width:10px;flex:none}
.why-list{position:absolute;left:533px;top:31px;list-style:none;font-size:8.5px;color:#d6e0f0}
.why-list li{display:flex;gap:5px;align-items:center;height:19.5px}
.why-list li span.ic{width:8px;height:8px;border-radius:50%;background:#d6e0f0}
.copyright{position:absolute;left:70px;top:150px;font-size:7px;color:#a9bbd9}
.pay{position:absolute;left:517px;top:150px;font-size:7px;color:#a9bbd9}
.pay-card{position:absolute;top:146px;width:30px;height:18px;border-radius:2px}
</style>
</head>
<body>

<header class="site-header">
  <div class="brand"><span class="brand-dot"></span><span class="brand-name">NetQuarry</span></div>
  <div class="header-item" style="left:270px">
    <svg width="12" height="12" viewBox="0 0 12 12"><path d="M2 1l2 0 1 3-1.5 1c.7 1.5 1.8 2.6 3.3 3.3L8 7l3 1v2c0 .6-.5 1-1 1C5 11 1 7 1 2c0-.5.4-1 1-1z" fill="none" stroke="#f7892b" stroke-width="1"/></svg>
    <div><strong>(+61) 02 5550 4172</strong><span>nq.sales@example.com</span></div>
  </div>
  <div class="header-item" style="left:387px">
    <svg width="11" height="12" viewBox="0 0 11 12"><circle cx="5.5" cy="3.5" r="2.6" fill="none" stroke="#f7892b"/><path d="M1 11.5c0-3 2-4.5 4.5-4.5S10 8.5 10 11.5z" fill="none" stroke="#f7892b"/></svg>
    <div><strong>Customer Account</strong><span>Signup or purchse now</span></div>
  </div>
  <div class="header-item" style="left:505px">
    <svg width="13" height="11" viewBox="0 0 13 11"><path d="M1 3h11l-1.5 7h-8z M4 3l2.5-2.5L9 3" fill="none" stroke="#f7892b"/></svg>
    <div><strong>Shopping Cart</strong><span>(0)Items - $0.00</span></div>
  </div>
  <div class="quote-btn">Request A Quote</div>
</header>

<nav class="main-nav">
  <ul>
    <li class="active">Home</li><li>Routers</li><li>Switches</li><li>Wirelesses</li><li>IP Phones</li><li>Accessories</li>
  </ul>
  <div class="search">Search with product name...
    <svg width="10" height="10" viewBox="0 0 10 10"><circle cx="4" cy="4" r="3" fill="none" stroke="#bbb"/><path d="M6.3 6.3L9 9" stroke="#bbb"/></svg>
  </div>
</nav>

<section class="hero">
  <svg class="hero-swoosh" width="754" height="296"><path d="M330 296C470 200 600 150 754 150V296z" fill="#fff" opacity=".55"/><path d="M420 0C520 90 640 110 754 90V0z" fill="#fff" opacity=".35"/></svg>
  <div class="hero-art" role="img" aria-label="Row of rack-mounted networking chassis, routers and switches"></div>
  <div class="hero-title">Save Up To <b>40%</b></div>
  <div class="hero-sub">By doing business with <em>NETQUARRY</em></div>
  <div class="stock-btn">Stock List<i></i></div>
  <div class="dots"><span class="on"></span><span></span><span></span><span></span><span></span></div>
</section>

<section class="categories">
  <div class="section-title-light">PRODUCT CATEGORIES</div>
  <div class="cat-card active" style="left:70px"><div class="cat-thumb" role="img" aria-label="Wireless controller and access points"></div><div class="cat-name">Wireless &amp;<br>Securiries</div></div>
  <div class="cat-card" style="left:225px"><div class="cat-thumb" role="img" aria-label="Stacked routers and switches"></div><div class="cat-name">Routers &amp;<br>Switches</div></div>
  <div class="cat-card" style="left:379px"><div class="cat-thumb" role="img" aria-label="Desk IP phones"></div><div class="cat-name">IP Phones</div></div>
  <div class="cat-card" style="left:534px"><div class="cat-thumb" role="img" aria-label="Transceiver modules and cables"></div><div class="cat-name">Accessories</div></div>
  <div class="pointer"></div>
</section>

<section class="products">
  <div class="product-card" style="left:70px"><div class="product-img" role="img" aria-label="White wireless access point"></div><div class="product-name">VNX-AP6120-A-K2</div><div class="price">New : <b>A$520</b><br>Refferbished : <b>A$220</b></div><div class="save">(Save : $A300 - 30%)</div></div>
  <div class="product-card" style="left:227px"><div class="product-img" role="img" aria-label="Dark rack-mount router"></div><div class="product-name">VNX-AP6120-A-K2</div><div class="price">New : <b>A$520</b><br>Refferbished : <b>A$220</b></div><div class="save">(Save : $A300 - 30%)</div></div>
  <div class="product-card" style="left:385px"><div class="product-img" role="img" aria-label="Small desktop router"></div><div class="product-name">VNX-AP6120-A-K2</div><div class="price">New : <b>A$520</b><br>Refferbished : <b>A$220</b></div><div class="save">(Save : $A300 - 30%)</div></div>
  <div class="product-card" style="left:542px"><div class="product-img" role="img" aria-label="Rack-mount security appliance"></div><div class="product-name">VNX-AP6120-A-K2</div><div class="price">New : <b>A$520</b><br>Refferbished : <b>A$220</b></div><div class="save">(Save : $A300 - 30%)</div></div>
  <div class="view-more">View More Products</div>
</section>

<section class="welcome">
  <h2 class="welcome-title">WELCOME TO NETQUARRY</h2>
  <div class="stat" style="top:752px"><span class="num">7</span><span class="lbl">Years of<br>Experience</span></div>
  <div class="stat" style="top:795px"><span class="num">99.5<small>%</small></span><span class="lbl">Positive Feedback<br>On Tradeloft</span></div>
  <div class="stat" style="top:837px"><span class="num">300</span><span class="lbl">Clients &amp; Partners<br>Around The World</span></div>
  <div class="stat last" style="top:888px"><span class="num">1.250</span><span class="lbl">SKUs In<br>Inventory</span></div>
  <p class="about-text">With over fifteen years experience selling and buying new and used networking equipment, NetQuarry is one of the most preeminet and longest established businesses in the global reseller marketplace. The manufacturers that we specials in include; <strong>VORNEX, Kestrel ( New Products Only), Norvane, Aveline, Halcyon, Trecom, Forgeline, Entrix, Brocara and Packetry.</strong></p>
  <div class="read-more">Read More</div>
  <aside class="quote-box">
    <div class="agent" role="img" aria-label="Customer service agent wearing a headset"></div>
    <div class="quote-corner"></div>
    <div class="quote-body">
      <h3>REQUEST A QUOTE</h3>
      <div class="quote-phone">(061) 02 5550 4172</div>
      <div class="quote-note">Call today for a gret price on new and used networking equipment</div>
      <div class="quote-or">Or email to:</div>
      <div class="quote-mail">nq.sales@example.com</div>
    </div>
  </aside>
</section>

<a class="policy" style="left:70px;background:var(--orange)">WARRANTY <i></i></a>
<a class="policy" style="left:277px;background:var(--blue)">PRIVACY STATMENT <i></i></a>
<a class="policy" style="left:484px;background:var(--yellow)">TERMS OF TRADE <i></i></a>

<footer class="site-footer">
  <div class="footer-title" style="left:70px;top:17px">ABOUT US</div>
  <p class="footer-about">Class aptent taciti sociosqu ad litora torquent per conubia nostra, per inceptos himenaeos. Mauris in erat justo. Nullam ac urna eu felis dapibus condimentum sit amet a augue. Sed non neque elit. Sed ut imperdiet nisi. Class aptent taciti sociosqu ad litora torquent per conubia nostra, per inceptos himenaeos.</p>
  <div class="footer-title" style="left:280px;top:17px">CONTACT US</div>
  <ul class="contact-list">
    <li><svg viewBox="0 0 10 10" height="10"><path d="M5 9.5C3 7 2 5.5 2 4a3 3 0 016 0c0 1.5-1 3-3 5.5z" fill="#b9c8e2"/></svg>Unit 9/12B Harlow St Marrickvale,NSW 2199</li>
    <li><svg viewBox="0 0 10 10" height="10"><path d="M2 1h2l1 2.5-1.3.8c.6 1.3 1.5 2.2 2.8 2.8L7.3 6 10 7v2c0 .5-.5 1-1 1C4.5 10 0 5.5 0 1.5c0-.5.5-.5 1-.5z" fill="none" stroke="#b9c8e2"/></svg>(+61) 25 550 4172/04 5550 9183</li>
    <li><svg viewBox="0 0 10 10" height="10"><circle cx="5" cy="5" r="4" fill="none" stroke="#b9c8e2"/><path d="M5 2.5V5h2" stroke="#b9c8e2" fill="none"/></svg>8:30am - 5:30pm / Mon - Fri(UTC+10)</li>
    <li><svg viewBox="0 0 10 10" height="10"><rect x="1" y="2.5" width="8" height="5.5" fill="none" stroke="#b9c8e2"/><path d="M1 2.5l4 3 4-3" fill="none" stroke="#b9c8e2"/></svg>sales@netquarry-example.com.au</li>
    <li><svg viewBox="0 0 10 10" height="10"><rect x="1" y="3" width="8" height="4" rx="1" fill="#b9c8e2"/></svg>http://stores.tradeloft-example.com.au/netquarry0255504172</li>
  </ul>
  <div class="footer-title" style="left:533px;top:14px">WHY US</div>
  <ul class="why-list">
    <li><span class="ic"></span>100% Wholesale Price</li>
    <li><span class="ic"></span>100% Quality Assurance</li>
    <li><span class="ic"></span>Free Support</li>
    <li><span class="ic"></span>100% Money Back Guarantee</li>
    <li><span class="ic"></span>Flexible Payment</li>
  </ul>
  <div class="copyright">©2010-2017 NetQuarry Pty Ltd.</div>
  <div class="pay">Payment Method</div>
  <div class="pay-card" style="left:592px;background:#fff"></div>
  <div class="pay-card" style="left:624px;background:#fff"></div>
  <div class="pay-card" style="left:656px;background:#d9372b"></div>
</footer>

</body>
</html>
```